Stunning Infographic - Value Model

I need an Infographic designed to represent my business model for a niche product I am taking to market.
The graphic will be used on my website and various landing pages and will clearly display my "Value Model"
I have some ideas of how it may look conceptually however am also open to unique design approaches.
See CREATIVE BRIEF within the attached.
Updates

Target Market(s)

Accommodation Business Owners (Hotels, Motels, BnB's)

Industry/Entity Type

Hospitality

Font styles to use
Sans Serif

Requirements
Must have
• Fresh Graphic that pops off the page!!
• Use of Hotel Icon to portray the industry.
• Demonstrate Accension
Nice to have
• Not sure
Should not have
• Not sure

```html
<!DOCTYPE html>
<html lang="en">
<head>
<meta charset="utf-8">
<title>63 Day Hotel Rescue Roadmap</title>
<link href="https://fonts.googleapis.com/css2?family=Roboto:wght@300;400;500;700&family=Roboto+Condensed:wght@400;700&display=swap" rel="stylesheet">
<style>
  :root {
    --bg: #eef2f4;
    --bg-light: #fbfcfd;
    --title-blue: #3aa0d8;
    --title-grey: #6b6e72;
    --heading: #4e5256;
    --body: #55595d;
    --rule: #a8acb0;
    --axis: #7f8387;
    --py-orange: #f7913a;
    --py-green: #b2d46a;
    --py-teal: #5cc3b7;
    --py-blue: #3aa3dc;
    --band-orange: #da8332;
    --band-orange-dark: #8c4c1c;
    --band-green: #8cae4d;
    --band-green-dark: #4d6c2a;
    --band-teal: #2ba39f;
    --band-teal-dark: #12676a;
    --band-blue: #3b80c4;
    --band-blue-dark: #23558f;
    --hotel-wing: #8b98cf;
    --hotel-tower: #4f5a7e;
    --white: #ffffff;
  }
  html, body { margin: 0; padding: 0; overflow: hidden; }
  body { width: 1200px; height: 900px; background: var(--bg); }
  .roadmap {
    position: relative; width: 1200px; height: 900px; overflow: hidden;
    background: radial-gradient(ellipse at 50% 45%, var(--bg-light) 0%, var(--bg) 70%);
    font-family: "Roboto", Arial, sans-serif;
  }
  .roadmap-art { position: absolute; inset: 0; }
  .roadmap-title {
    position: absolute; top: 78px; left: 0; width: 1200px; margin: 0;
    text-align: center; font-size: 46px; font-weight: 300; color: var(--title-grey); letter-spacing: 0.5px;
  }
  .roadmap-title strong { color: var(--title-blue); font-weight: 700; }
  .column-heading {
    position: absolute; top: 190px; margin: 0;
    font-size: 29px; font-weight: 700; color: var(--heading); letter-spacing: 0.5px;
  }
  .column-heading.symptoms { left: 225px; }
  .column-heading.keys { left: 732px; }
  .symptom { position: absolute; margin: 0; }
  .symptom h3 { margin: 0 0 5px; font-size: 14.5px; font-weight: 500; color: var(--heading); white-space: nowrap; }
  .symptom p { margin: 0; font-size: 13.3px; line-height: 19.6px; color: var(--body); font-weight: 400; }
  .stage-label { font-family: "Roboto Condensed", sans-serif; font-weight: 700; fill: var(--white); text-anchor: middle; letter-spacing: 1px; }
  .stage-label-small { font-family: "Roboto Condensed", sans-serif; font-weight: 400; font-size: 14.5px; fill: var(--white); text-anchor: middle; letter-spacing: 0.5px; }
  .stage-occ { font-family: "Roboto", sans-serif; font-weight: 500; fill: var(--white); text-anchor: middle; }
  .key-num { font-family: "Roboto Condensed", sans-serif; font-weight: 700; font-size: 52px; fill: var(--white); fill-opacity: 0.35; }
  .key-title { font-family: "Roboto Condensed", sans-serif; font-weight: 700; font-size: 27px; fill: var(--white); letter-spacing: 0.5px; }
  .key-line { font-family: "Roboto", sans-serif; font-size: 14.5px; fill: var(--white); }
  .axis-label { font-family: "Roboto", sans-serif; font-size: 21px; font-weight: 500; fill: var(--heading); text-anchor: middle; letter-spacing: 0.5px; }
  .axis-step { font-family: "Roboto", sans-serif; font-size: 11px; fill: var(--axis); text-anchor: middle; letter-spacing: 0.5px; }
  .hotel-sign { font-family: "Roboto", sans-serif; font-weight: 700; font-size: 25px; fill: var(--white); text-anchor: middle; letter-spacing: 1px; }
</style>
</head>
<body>
<main class="roadmap">
  <svg class="roadmap-art" width="1200" height="900" viewBox="0 0 1200 900">
    <defs>
      <linearGradient id="grad-boom" gradientUnits="userSpaceOnUse" x1="647" y1="0" x2="830" y2="0">
        <stop offset="0" stop-color="var(--band-orange-dark)"/><stop offset="1" stop-color="var(--band-orange)"/>
      </linearGradient>
      <linearGradient id="grad-boost" gradientUnits="userSpaceOnUse" x1="715" y1="0" x2="900" y2="0">
        <stop offset="0" stop-color="var(--band-green-dark)"/><stop offset="1" stop-color="var(--band-green)"/>
      </linearGradient>
      <linearGradient id="grad-bolster" gradientUnits="userSpaceOnUse" x1="783" y1="0" x2="965" y2="0">
        <stop offset="0" stop-color="var(--band-teal-dark)"/><stop offset="1" stop-color="var(--band-teal)"/>
      </linearGradient>
      <linearGradient id="grad-basics" gradientUnits="userSpaceOnUse" x1="852" y1="0" x2="1035" y2="0">
        <stop offset="0" stop-color="var(--band-blue-dark)"/><stop offset="1" stop-color="var(--band-blue)"/>
      </linearGradient>
      <linearGradient id="grad-hotel" x1="0" y1="0" x2="1" y2="0">
        <stop offset="0" stop-color="var(--hotel-wing)"/>
        <stop offset="0.3" stop-color="var(--hotel-tower)"/>
        <stop offset="0.7" stop-color="var(--hotel-tower)"/>
        <stop offset="1" stop-color="var(--hotel-wing)"/>
      </linearGradient>
    </defs>

    <g class="brackets" fill="none" stroke="var(--rule)" stroke-width="2">
      <polyline points="54,432 54,208 182,208"/>
      <circle cx="189" cy="208" r="7" fill="var(--bg-light)"/>
      <polyline points="1018,208 1144,208 1144,292"/>
      <circle cx="1011" cy="208" r="7" fill="var(--bg-light)"/>
    </g>

    <g class="key-bands">
      <rect x="640" y="292" width="528" height="110" fill="url(#grad-boom)"/>
      <rect x="700" y="402" width="468" height="110" fill="url(#grad-boost)"/>
      <rect x="770" y="512" width="398" height="110" fill="url(#grad-bolster)"/>
      <rect x="840" y="622" width="328" height="110" fill="url(#grad-basics)"/>
    </g>

    <g class="pyramid">
      <polygon points="602,220 683,350 522,350" fill="var(--py-orange)"/>
      <polygon points="522,350 683,350 762,478 444,478" fill="var(--py-green)"/>
      <polygon points="444,478 762,478 842,606 365,606" fill="var(--py-teal)"/>
      <polygon points="365,606 842,606 920,732 288,732" fill="var(--py-blue)"/>
    </g>

    <g class="stage-labels">
      <text class="stage-label-small" x="602" y="295">PROFIT</text>
      <text class="stage-label-small" x="602" y="313">OPTIMIZATION</text>
      <text class="stage-occ" x="602" y="335" font-size="12">80%+ Occupancy</text>

      <text class="stage-label" x="602" y="399" font-size="27">DEMAND</text>
      <text class="stage-label" x="602" y="426" font-size="27">GENERATION</text>
      <text class="stage-occ" x="602" y="452" font-size="15.5">60-80% Occupancy</text>

      <text class="stage-label" x="530" y="539" font-size="27">COMMODOTISATION</text>
      <text class="stage-occ" x="530" y="566" font-size="15.5">40-60% Occupancy</text>

      <text class="stage-label" x="453" y="669" font-size="29">LIQUIDATION</text>
      <text class="stage-occ" x="453" y="698" font-size="15.5">&lt;40% Occupancy</text>
    </g>

    <rect class="hotel-icon" x="574" y="592" width="230" height="224" fill="url(#grad-hotel)" role="img" aria-label="Hotel building icon with windows, entrance, red carpet and two small trees"/>
    <text class="hotel-sign" x="690" y="582">HOTEL</text>

    <g class="key-1">
      <text class="key-num" x="712" y="368">1</text>
      <text class="key-title" x="753" y="328">BOOM</text>
      <text class="key-line" x="753" y="348">Dynamic Pricing</text>
      <text class="key-line" x="753" y="368">Guest Engagement</text>
      <text class="key-line" x="753" y="388">Systems with purpose</text>
    </g>
    <g class="key-2">
      <text class="key-num" x="771" y="477">2</text>
      <text class="key-title" x="813" y="437">BOOST</text>
      <text class="key-line" x="813" y="457">Expanding Distribution</text>
      <text class="key-line" x="813" y="477">Knowing your Numbers</text>
      <text class="key-line" x="813" y="497">Increasing online Rankings</text>
    </g>
    <g class="key-3">
      <text class="key-num" x="837" y="586">3</text>
      <text class="key-title" x="883" y="546">BOLSTER</text>
      <text class="key-line" x="883" y="566">Reposition your Business</text>
      <text class="key-line" x="883" y="586">Your Story, Your Website</text>
      <text class="key-line" x="883" y="606">3 Online Actions that matter MOST</text>
    </g>
    <g class="key-4">
      <text class="key-num" x="902" y="696">4</text>
      <text class="key-title" x="946" y="657">BASICS</text>
      <text class="key-line" x="946" y="678">Re-learn the Industry</text>
      <text class="key-line" x="946" y="698">Know your Market &amp; your Gaps</text>
      <text class="key-line" x="946" y="718">Focus on the Quick Wins</text>
    </g>

    <g class="visibility-axis" transform="translate(240,732) rotate(-58.2)">
      <line x1="0" y1="0" x2="112" y2="0" stroke="var(--axis)" stroke-width="6" stroke-dasharray="2 2.5"/>
      <line x1="512" y1="0" x2="622" y2="0" stroke="var(--axis)" stroke-width="6" stroke-dasharray="2 2.5"/>
      <polyline points="614,-9 628,0 614,9" fill="none" stroke="var(--axis)" stroke-width="2.5"/>
      <text class="axis-label" x="312" y="8">ONLINE VISIBILITY &amp; BOOKABILITY</text>
      <text class="axis-step" x="75" y="28">INVISIBLE</text>
      <text class="axis-step" x="228" y="28">UNLIKELY</text>
      <text class="axis-step" x="378" y="28">PROMINENT</text>
      <text class="axis-step" x="536" y="28">POPULAR</text>
    </g>
  </svg>

  <h1 class="roadmap-title"><strong>63 DAY</strong> HOTEL RESCUE ROADMAP</h1>
  <h2 class="column-heading symptoms">SYMPTOMS</h2>
  <h2 class="column-heading keys">KEYS TO SUCCESS</h2>

  <section class="symptom" style="left:160px; top:250px; width:306px;">
    <h3>Maximised Potential, Profits &amp; Proficiency</h3>
    <p>High Occupancy, strong booking pace, demand is predictable and reliable. Confidence in how to promote, price &amp; performance manage your hotel.</p>
  </section>
  <section class="symptom" style="left:118px; top:356px; width:280px;">
    <h3>Rising Revenues &amp; Online Rankings</h3>
    <p>Steady Booking Flow, more and more automated, 1st page on most search results. Growing knowledge of what levers make a difference to occupancy demand.</p>
  </section>
  <section class="symptom" style="left:72px; top:486px; width:245px;">
    <h3>Out Competed &amp; Beaten to the Booking</h3>
    <p>Booking flow is trickling, difficult to be found online, paying high commissions to OTA’s. Limited understanding of modern hotel marketing.</p>
  </section>
  <section class="symptom" style="left:36px; top:619px; width:232px;">
    <h3>Bewildered &amp; Barely Breaking Even</h3>
    <p>Booking flow is extremely slow; little technology adoption; no idea where to start with making a change.</p>
  </section>
</main>
</body>
</html>
```